Website Design

Hi I would like to invite designers to re design my website .

I would like the below in brief.

On the Welcome Page.

A nice looking technical page distributed into two

SALES on one side and TECHNOLOGY on the other . once the person clicks on either of them they can explore the pages in detail.

I am keen and almost ready with information for the Technology page and would like this to begin kicking ASAP .

my current website is www.plumvesta.net

Looking forward to seeing your feedback!

Oduya
Updates

Hi,

 
A little more elaboration on the web front page . I need it to be more techy .

I was looking at a wheel on the Technical side or a spanner and screew driver done on flash .

Just to give you a better idea on what seperated Sales from Technology. 

Sales 

Computing, Storage , Components , Peripherals , Software , TV & Gaming / Entertainment , Home & Leisure , Software , Gift Vouchers , Phones etc.

Technology .

Solar Power Solutions , Security Systems , Access Control , Automatic Gates & Turnstiles , Home/Office/Hotel Automation, Indoor and Outdoor PABX Telephony, Networking , Electricity Power Meters , IP Based Technology and ETC. 

See attached on the project updates my business card design if it can give you an idea ,also see revised Logo 

Industry/Entity Type

Sales

```html
<!DOCTYPE html>
<html lang="en">
<head>
<meta charset="utf-8">
<title>Plumvesta — Home</title>
<link href="https://fonts.googleapis.com/css2?family=Lato:wght@300;400;700;900&family=Open+Sans:wght@400;600;700&display=swap" rel="stylesheet">
<style>
:root{
  --red:#c8262c;
  --navy:#1f2d37;
  --navy-2:#233540;
  --footer-bar:#1a252d;
  --grey-bg:#f1f1f1;
  --line:#d9d9d9;
  --text:#444;
  --muted:#8a8a8a;
  --white:#fff;
}
*{box-sizing:border-box;margin:0;padding:0}
html,body{width:1200px;height:2200px;overflow:hidden}
body{position:relative;background:var(--white);font-family:"Open Sans",Arial,sans-serif;color:var(--text)}
.abs{position:absolute}

/* header */
.site-header{left:0;top:0;width:1200px;height:132px;background:var(--white);border-bottom:1px solid var(--line)}
.topline{left:124px;top:6px;font-size:10px;color:var(--muted)}
.social-top{left:950px;top:5px;display:flex;gap:10px}
.social-top span{width:20px;height:20px;background:#d4d4d4;border-radius:2px;display:block}
.brand{left:124px;top:58px;font-family:"Lato",sans-serif;font-weight:900;font-size:42px;color:var(--red);letter-spacing:.5px}
.main-nav{left:437px;top:32px;display:flex;height:100px}
.main-nav a{display:block;padding:26px 12px 0;font-family:"Lato",sans-serif;font-size:11px;font-weight:700;letter-spacing:1.2px;color:#888;text-decoration:none;border-top:3px solid transparent}
.main-nav a.active{color:var(--red);border-top-color:var(--red)}
.nav-search{left:1028px;top:58px}

/* hero */
.hero{left:0;top:132px;width:1200px;height:423px}
.hero-sales{left:0;top:0;width:600px;height:423px;background:var(--navy)}
.hero-tech{left:600px;top:0;width:600px;height:423px;background:radial-gradient(circle at 60% 40%,#d8343a 0%,var(--red) 45%,#a71c22 100%)}
.sales-title{left:86px;top:92px;font-family:"Lato",sans-serif;font-weight:700;font-size:100px;line-height:1;color:var(--white);letter-spacing:1px}
.sales-rule{left:88px;top:206px;width:310px;height:1px;background:rgba(255,255,255,.35)}
.sales-sub{left:88px;top:220px;font-family:"Lato",sans-serif;font-size:30px;color:var(--white)}
.tech-title{left:600px;top:92px;width:600px;text-align:center;font-family:"Lato",sans-serif;font-weight:700;font-size:34px;color:var(--white);letter-spacing:1px}
.tech-steps{left:600px;top:155px;width:600px;height:120px}
.tech-label{top:222px;width:140px;text-align:center;font-family:"Lato",sans-serif;font-weight:700;font-size:14px;color:var(--white)}
.btn-view{left:512px;top:354px;width:176px;height:42px;border:2px solid var(--white);color:var(--white);font-family:"Lato",sans-serif;font-weight:900;font-size:13px;letter-spacing:1px;display:flex;align-items:center;justify-content:center}

/* sections */
.section-rule{left:0;top:596px;width:1200px;height:1px;background:var(--line)}
.section-title{width:1200px;left:0;text-align:center;font-family:"Lato",sans-serif;font-size:21px;font-weight:400;letter-spacing:1px;color:#555;text-transform:uppercase}
.section-title b{color:var(--red);font-weight:900}
.title-notch{width:50px;height:1px;background:var(--line);left:575px}
.intro-text{left:220px;top:684px;width:760px;text-align:center;font-size:14px;line-height:22px;color:#555}
.services{left:0;top:851px;width:1200px;height:386px;background:var(--grey-bg);border-top:1px solid var(--line)}

/* newsletter */
.newsletter{left:0;top:1237px;width:1200px;height:132px;background:var(--navy-2)}
.nl-head{top:50px;font-family:"Lato",sans-serif;font-weight:900;font-size:11px;letter-spacing:1px;color:var(--white)}
.nl-text{left:218px;top:68px;font-size:10px;color:#ccd5dc}
.nl-input{left:610px;top:52px;width:226px;height:32px;border:1px solid #aab;color:#dde;font-size:11px;padding:8px 10px}
.nl-btn{left:843px;top:52px;width:137px;height:32px;border:1px solid #dde;color:var(--white);font-family:"Lato",sans-serif;font-weight:900;font-size:11px;letter-spacing:1px;display:flex;align-items:center;justify-content:center}

/* blog */
.post{top:1457px;width:176px;height:230px}
.post-image{width:176px;height:128px;border-bottom:4px solid var(--red)}
.post-body{top:154px;left:0;width:176px;height:76px;border:1px solid #e2e2e2;border-bottom:none;text-align:center;padding:12px 10px 0}
.post-title{font-family:"Lato",sans-serif;font-weight:900;font-size:12px;letter-spacing:.5px;color:#333}
.post-excerpt{font-size:9.5px;line-height:13px;color:#666;margin-top:5px}
.post-notch{left:78px;top:132px;width:0;height:0;border-left:10px solid transparent;border-right:10px solid transparent;border-top:10px solid var(--red)}

/* testimonial */
.testimonial{left:0;top:1740px;width:1200px;height:198px;background:radial-gradient(circle at 35% 50%,#d9353b 0%,var(--red) 50%,#9f1a20 100%)}
.avatar{left:220px;top:58px;width:84px;height:84px;border:3px solid var(--white);background:linear-gradient(160deg,#c9b8a8,#8d7461)}
.avatar-rule{left:318px;top:50px;width:1px;height:100px;background:rgba(255,255,255,.4)}
.quote{left:346px;top:64px;width:600px;font-size:18px;line-height:26px;color:var(--white)}
.quote-by{left:346px;top:122px;font-size:11px;color:var(--white);font-weight:700}
.quote-by span{color:#f0b0b0;font-weight:400}
.arrow{top:88px}

/* footer */
.site-footer{left:0;top:1938px;width:1200px;height:220px;background:var(--navy-2)}
.f-col{top:56px}
.f-head{font-family:"Lato",sans-serif;font-weight:700;font-size:13px;letter-spacing:1px;color:#e6e9ec;display:flex;align-items:center;gap:10px}
.f-head i{display:block;width:30px;height:16px;background:#3d6e9a}
.f-text{font-size:10px;line-height:14px;color:#9aa6ae;margin-top:14px;width:230px}
.f-row{font-size:9.5px;color:#9aa6ae;margin-top:9px;display:flex;gap:14px}
.f-row b{color:#c5ccd1;width:56px;font-weight:700;letter-spacing:.5px}
.f-input{width:170px;height:28px;border:1px solid #aab;font-size:10px;color:#dde;padding:6px 8px}
.f-btn{width:64px;height:28px;border:1px solid #dde;color:var(--white);font-size:10px;font-weight:700;display:flex;align-items:center;justify-content:center}
.footer-bar{left:0;top:2158px;width:1200px;height:42px;background:var(--footer-bar)}
.copyright{left:220px;top:16px;font-size:8px;letter-spacing:1px;color:#607078}
.social-foot{left:866px;top:10px;display:flex;gap:14px}
.social-foot span{width:22px;height:22px;background:#3a4a55;display:block}
</style>
</head>
<body>

<header class="abs site-header">
  <div class="abs topline">Email Us: hello@plumvesta.net | Call Us: 123-456-7890</div>
  <div class="abs social-top"><span></span><span></span><span></span><span></span></div>
  <div class="abs brand">Plumvesta</div>
  <nav class="abs main-nav">
    <a class="active">HOME</a><a>PORTFOLIO</a><a>BLOG</a><a>PAGES</a><a>SHOP</a><a>MEGA MENU</a><a>CONTACT</a>
  </nav>
  <svg class="abs nav-search" width="16" height="16" viewBox="0 0 18 18"><circle cx="7.5" cy="7.5" r="5.5" fill="none" stroke="#777" stroke-width="2"/><line x1="11.5" y1="11.5" x2="16" y2="16" stroke="#777" stroke-width="2"/></svg>
</header>

<section class="abs hero">
  <div class="abs hero-sales"></div>
  <div class="abs hero-tech" role="img" aria-label="Red circuit board photograph"></div>
  <div class="abs sales-title">SALES</div>
  <div class="abs sales-rule"></div>
  <div class="abs sales-sub">Visit our Shop Now</div>

  <div class="abs tech-title">TECHNOLOGY</div>
  <svg class="abs tech-steps" width="600" height="120" viewBox="0 0 600 120">
    <line x1="155" y1="10" x2="445" y2="10" stroke="#fff" stroke-opacity=".6" stroke-width="1"/>
    <circle cx="155" cy="10" r="5" fill="#fff"/><circle cx="300" cy="10" r="5" fill="#fff"/><circle cx="445" cy="10" r="5" fill="#fff"/>
    <g fill="#fff">
      <rect x="146" y="32" width="3" height="26"/><path d="M149 32h18l-4 6 4 6h-18z"/>
      <rect x="288" y="33" width="24" height="24" rx="5" fill="none" stroke="#fff" stroke-width="3"/>
      <rect x="294" y="39" width="5" height="5"/><rect x="301" y="39" width="5" height="5"/><rect x="294" y="46" width="5" height="5"/><rect x="301" y="46" width="5" height="5"/>
      <circle cx="445" cy="45" r="9" fill="none" stroke="#fff" stroke-width="5" stroke-dasharray="4 3"/><circle cx="445" cy="45" r="6" fill="none" stroke="#fff" stroke-width="3"/>
    </g>
  </svg>
  <div class="abs tech-label" style="left:685px">Branding</div>
  <div class="abs tech-label" style="left:830px">UX Design</div>
  <div class="abs tech-label" style="left:975px">Develop</div>
  <div class="abs btn-view">VIEW WORK</div>
</section>

<div class="abs section-rule"></div>
<h2 class="abs section-title" style="top:628px">Branding that makes an <b>impact</b></h2>
<div class="abs title-notch" style="top:662px"></div>
<p class="abs intro-text">Lorem ipsum dolor sit amet, consectetur adipiscing elit. Sed ut purus eget nunc dignissim cursus at a nisl. Mauris vitae turpis quis eros egestas tempor sit amet a arcu.</p>

<section class="abs services" aria-label="Services"></section>
<h2 class="abs section-title" style="top:916px">Our outstanding <b>services</b></h2>
<div class="abs title-notch" style="top:950px"></div>

<section class="abs newsletter">
  <svg class="abs" style="left:218px;top:50px" width="14" height="11" viewBox="0 0 14 11"><rect x="1" y="1" width="12" height="9" fill="none" stroke="#fff" stroke-width="1.5"/><path d="M1 1l6 5 6-5" fill="none" stroke="#fff" stroke-width="1.5"/></svg>
  <div class="abs nl-head" style="left:240px">SUBSCRIBE TO OUR NEWSLETTER</div>
  <div class="abs nl-text">Lorem ipsum dolor sit amet, consectetur adipiscing elit. Sed ut purus eget nunc.</div>
  <div class="abs nl-input">Your email</div>
  <div class="abs nl-btn">SUBSCRIBE</div>
</section>

<h2 class="abs section-title" style="top:1382px">Recent <b>blog</b> posts</h2>
<div class="abs title-notch" style="top:1416px"></div>

<article class="abs post" style="left:220px">
  <div class="post-image" role="img" aria-label="Blue toned close-up of a small gadget" style="background:linear-gradient(160deg,#3a7fa5,#123346)"></div>
  <div class="abs post-notch"></div>
  <div class="abs post-body"><div class="post-title">THIS IS A POST TITLE</div><div class="post-excerpt">Lorem ipsum dolor sit amet, consectetur adipiscing elit. Sed ut purus eget nunc cursus</div></div>
</article>
<article class="abs post" style="left:415px">
  <div class="post-image" role="img" aria-label="City lights at night under a teal sky" style="background:linear-gradient(180deg,#2d6f80,#1a2a30 60%,#c09a50)"></div>
  <div class="abs post-notch"></div>
  <div class="abs post-body"><div class="post-title">THIS IS A POST TITLE</div><div class="post-excerpt">Lorem ipsum dolor sit amet, consectetur adipiscing elit. Sed ut purus eget nunc cursus</div></div>
</article>
<article class="abs post" style="left:609px">
  <div class="post-image" role="img" aria-label="Black and white photo of hands holding a camera" style="background:linear-gradient(160deg,#6a6a6a,#151515)"></div>
  <div class="abs post-notch"></div>
  <div class="abs post-body"><div class="post-title">THIS IS A POST TITLE</div><div class="post-excerpt">Lorem ipsum dolor sit amet, consectetur adipiscing elit. Sed ut purus eget nunc cursus</div></div>
</article>
<article class="abs post" style="left:804px">
  <div class="post-image" role="img" aria-label="Black and white photo of chess pieces" style="background:linear-gradient(180deg,#e8e8e8,#5a5a5a)"></div>
  <div class="abs post-notch"></div>
  <div class="abs post-body"><div class="post-title">THIS IS A POST TITLE</div><div class="post-excerpt">Lorem ipsum dolor sit amet, consectetur adipiscing elit. Sed ut purus eget nunc cursus</div></div>
</article>

<section class="abs testimonial">
  <svg class="abs arrow" style="left:10px" width="14" height="24" viewBox="0 0 14 24"><path d="M12 2L2 12l10 10" fill="none" stroke="#fff" stroke-opacity=".5" stroke-width="2"/></svg>
  <svg class="abs arrow" style="left:1176px" width="14" height="24" viewBox="0 0 14 24"><path d="M2 2l10 10L2 22" fill="none" stroke="#fff" stroke-opacity=".5" stroke-width="2"/></svg>
  <div class="abs avatar" role="img" aria-label="Customer portrait photo"></div>
  <div class="abs avatar-rule"></div>
  <p class="abs quote">Lorem ipsum dolor sit amet, consectetur adipiscing elit. Sed ut purus eget nunc dignissim cursus at a nisl. Lorem ipsum dolor sit amet.</p>
  <div class="abs quote-by">JOHN DOE | <span>Client since 2014</span></div>
</section>

<footer class="abs site-footer">
  <div class="abs f-col" style="left:220px">
    <div class="f-head"><i></i>PLUMVESTA</div>
    <p class="f-text">Lorem ipsum dolor sit amet, consectetur adipiscing elit. Sed ut purus eget nunc at dignissim cursus at a nisl. Duis egestas hendrerit diam.</p>
  </div>
  <div class="abs f-col" style="left:481px">
    <div class="f-head">CONTACT</div>
    <div class="f-row" style="margin-top:14px"><b>ADDRESS:</b>45 Harbor Lane, Kestrel Bay</div>
    <div class="f-row"><b>TELEPHONE:</b>+1 (234) 567 8901</div>
    <div class="f-row"><b>EMAIL:</b>hello@plumvesta.net</div>
  </div>
  <div class="abs f-col" style="left:740px">
    <div class="f-head">NEWSLETTER</div>
    <p class="f-text">Lorem ipsum dolor sit amet, consectetur adipiscing elit. Sed ut purus.</p>
    <div style="display:flex;gap:6px;margin-top:8px"><div class="f-input">Your email</div><div class="f-btn">SEND</div></div>
  </div>
</footer>
<div class="abs footer-bar">
  <div class="abs copyright">PLUMVESTA COPYRIGHT 2014</div>
  <div class="abs social-foot"><span></span><span></span><span></span><span></span></div>
</div>

</body>
</html>
```